Boutique furnished offices with "high end" childcare centre require Wordpress website template

Project Overview: We require a wordpress design for a new company based in South Perth Western Australia, "The Harbour 19 Collective" which provide centres where parents can utilise childcare whilst hiring furnished offices and co-working spaces. We also provide onsite beauty, hair, gymnasium and park & ride facilities into the CBD which can all be booked online through our website (plugins required to be used to book through https://quickslotter.example/). We are a one stop shop where you can drop your children at childcare, skip the traffic and ride the ferry into the CBD. Or simply have your children cared for whilst you work out of our furnished office facilities.
The website design should be classy, modern, gender neutral and corporate (not too children focused/playful).

Look And Feel: clean, classy, modern site which is easy to navigate and book services online. It must also be gender neutral and corporate (not children focused/playful).
A typical childcare centre feel - we aren’t going for "jellybeans and teddybears" we are looking for a classy, corporate and sophisticated feel.

(LOGO currently being finalised but is charcoal grey on a white back ground and attached below - but will all be in lower case not capitals)

Target Market(s)

Target market is working parents, predominantly corporate or consultants running their own businesses.

Industry/Entity Type

Boutique

Number of Pages Required

2 page

Requirements
Must have
• The following would be required of the winning submission:
• • Clean, classy, modern site which is easy to navigate and book services online. It must also be gender neutral and corporate (not children focused/playful).
• • Require simplistic homepage with Menu of list of services, and template for individual pages for each of the services offered (child care, furnished offices, park & ride, hair/ beauty, gymnasium)
• • Necessary customization/plugins to allow online bookings to be placed https://quickslotter.example/
• • Well placed plugin/customization to link and also allow "share it" type links to major social networks (linkedin, facebook, twitter, google+, etc.).
• • All design components should be optimized for indexing on major search engines
• • Wordpress theme that is supported in Chrome, IE 8+, firefox, and safari
Nice to have
• Included below is a list of sites that we like from a simplicity and clean look and feel.
• http://www.lumenfold.example.au/
• http://www.wanderthegardenpath.example.uk/
• http://www.velopiccolo.example/
• http://www.qvframe.example.au/
• http://madebymarten.example/

```html
<!DOCTYPE html>
<html lang="en">
<head>
<meta charset="utf-8">
<title>The Harbour 19 Collective</title>
<link rel="stylesheet" href="https://fonts.googleapis.com/css2?family=Great+Vibes&family=Montserrat:wght@400;600;700&family=EB+Garamond:ital,wght@0,400;1,400&display=swap">
<style>
:root{
  --charcoal:#323031;
  --ink:#3a3a3a;
  --cream:#ede6c8;
  --sand:#d7bf6e;
  --yellow:#f2d31b;
  --blue:#1e88c8;
  --sky:#bfe6f8;
  --white:#ffffff;
  --muted:#777;
  --sage:#cdd2b2;
}
*{box-sizing:border-box;margin:0;padding:0}
html,body{width:1200px;height:3711px;overflow:hidden}
body{position:relative;background:var(--white);font-family:'Montserrat',sans-serif;color:var(--ink)}
.abs{position:absolute}
.caps{font-family:'Montserrat',sans-serif;text-transform:uppercase;letter-spacing:1px}
.serif{font-family:'EB Garamond',serif}

/* hero */
.hero{left:0;top:0;width:1200px;height:640px;background:linear-gradient(100deg,#dfe2c9 0%,#cdd3b0 45%,#b9bd98 70%,#c9c3a7 100%)}
.hero-cut{left:0;top:540px;width:1200px;height:110px}
.logo-panel{left:160px;top:0;width:273px;height:111px;background:rgba(255,255,255,.55);display:flex;align-items:center;justify-content:center}
.logo-text{font-family:'Montserrat',sans-serif;font-weight:600;font-size:19px;letter-spacing:1px;color:var(--charcoal)}
.topbar{left:480px;top:6px;height:24px;display:flex;align-items:center;gap:16px;font-size:12px;color:#555}
.topbar .sep{width:1px;height:14px;background:#999}
.search{left:858px;top:0;width:38px;height:34px;background:#555}
.socials-top{left:915px;top:7px;display:flex;gap:5px}
.socials-top span{width:20px;height:20px;border-radius:50%;background:var(--charcoal)}
.nav{left:640px;top:58px;display:flex;gap:28px;font-size:13px;font-weight:600;color:var(--charcoal)}
.hero-title{left:66px;top:225px;font-family:'Great Vibes',cursive;font-size:104px;color:var(--white);line-height:1}
.hero-sub{left:72px;top:340px;font-size:29px;font-weight:700;color:var(--white)}
.hero-btn{left:317px;top:406px;width:215px;height:64px;border:3px solid var(--white);color:var(--white);font-size:22px;font-weight:600;display:flex;align-items:center;justify-content:center;letter-spacing:1px}
.arrows{left:535px;top:584px}

/* section title frame */
.frame-title{left:0;width:1200px;text-align:center}
.frame-title .box{display:inline-block;position:relative;padding:8px 26px;font-family:'EB Garamond',serif;font-size:42px;letter-spacing:2px}
.frame-title .box::before,.frame-title .box::after{content:"";position:absolute;top:0;bottom:0;width:16px;border:3px solid var(--yellow)}
.frame-title .box::before{left:0;border-right:none}
.frame-title .box::after{right:0;border-left:none}
.intro{left:0;width:1200px;text-align:center;font-family:'EB Garamond',serif;font-style:italic;font-size:17px;line-height:1.6}
.rule{width:44px;height:3px;background:var(--yellow)}

/* about */
.about-title{top:706px;color:#b49a4a}
.about-intro{top:800px;color:#777}
.about-rule{left:578px;top:858px}
.about-text{left:198px;top:903px;width:804px;text-align:center;font-size:13.5px;line-height:1.75;color:#444}
.more-btn{left:541px;top:1032px;width:118px;height:30px;background:var(--yellow);font-family:'EB Garamond',serif;font-size:12px;font-weight:600;display:flex;align-items:center;justify-content:center;color:#222}

/* services */
.services{left:0;top:1101px;width:1200px;height:1472px;background:var(--charcoal)}
.services-title{top:1158px;color:var(--yellow)}
.services-intro{top:1254px;color:#ddd}
.card{width:270px;background:var(--cream);box-shadow:0 4px 10px rgba(0,0,0,.3)}
.card .photo{width:100%}
.card .tab{position:absolute;left:6px;right:6px;height:42px;background:var(--cream);display:flex;align-items:center;justify-content:center;font-weight:700;font-size:18px;letter-spacing:1.5px;color:#222}
.card .body{position:absolute;left:18px;right:18px;text-align:center;font-family:'EB Garamond',serif;font-size:15px;line-height:1.45;color:#444}
.card .btn{position:absolute;left:50%;margin-left:-30px;width:60px;height:27px;background:var(--blue);color:var(--white);font-size:12px;font-weight:600;display:flex;align-items:center;justify-content:center}
.book-btn{left:465px;top:2459px;width:268px;height:79px;border:3px solid var(--yellow);color:var(--yellow);font-size:23px;font-weight:700;letter-spacing:1px;display:flex;align-items:center;justify-content:center}

/* banner */
.banner{left:0;top:2573px;width:1200px;height:487px;background:linear-gradient(120deg,#dcc67c 0%,#cfb35e 45%,#c6aa55 70%,#dcc581 100%)}
.banner-title{left:0;top:2735px;width:1200px;text-align:center;font-size:54px;font-weight:700;letter-spacing:2px;color:var(--charcoal)}
.banner-rule{left:563px;top:2818px;width:74px;height:4px;background:var(--charcoal)}
.banner-text{left:250px;top:2850px;width:700px;text-align:center;font-family:'EB Garamond',serif;font-style:italic;font-size:19px;line-height:1.65;color:#2d2d2d}

/* map */
.map{left:0;top:3060px;width:1200px;height:441px;background:linear-gradient(160deg,#c9ecfb,#aedcf3)}
.contact-strip{left:161px;top:3394px;width:878px;height:107px;background:var(--white);display:flex;box-shadow:0 -2px 8px rgba(0,0,0,.12)}
.contact-strip .cell{flex:1;display:flex;align-items:center;justify-content:center;gap:18px;font-family:'EB Garamond',serif;font-size:19px;color:#333;border-right:1px solid #ddd}
.contact-strip .cell:last-child{border-right:none}

/* footer */
.foot-logo{left:203px;top:3545px;width:213px;height:40px;display:flex;align-items:center;justify-content:center;border-top:2px solid var(--charcoal);border-bottom:2px solid var(--charcoal)}
.foot-logo span{font-weight:600;font-size:14px;letter-spacing:1px;color:var(--charcoal)}
.news-label{left:465px;top:3534px;font-family:'EB Garamond',serif;font-size:15px;color:#333}
.news-input{left:465px;top:3575px;width:208px;height:33px;background:#e9e6d9;font-family:'EB Garamond',serif;font-size:13px;color:#999;padding-left:70px;display:flex;align-items:center}
.news-btn{left:673px;top:3575px;width:62px;height:33px;background:var(--yellow);font-size:11px;font-weight:700;color:var(--white);display:flex;align-items:center;justify-content:center}
.socials-foot{left:822px;top:3560px;display:flex;gap:8px}
.socials-foot span{width:30px;height:30px;border-radius:50%;background:var(--charcoal)}
.bottom-bar{left:0;top:3649px;width:1200px;height:62px;background:#262626;color:#aaa;font-family:'EB Garamond',serif;font-size:11px}
.bottom-bar .copy{position:absolute;left:173px;top:24px}
.bottom-bar .links{position:absolute;left:462px;top:24px;display:flex;gap:14px}
</style>
</head>
<body>

<!-- hero -->
<div class="abs hero" role="img" aria-label="Soft sage photograph of a child in aviator goggles holding up a wooden toy plane against a hazy field"></div>
<svg class="abs hero-cut" width="1200" height="110" viewBox="0 0 1200 110">
  <polygon points="0,40 410,95 600,40 1200,40 1200,110 0,110" fill="#ffffff" opacity="0"/>
  <polygon points="0,35 410,95 600,60 1200,0 1200,110 0,110" fill="#ffffff"/>
</svg>
<div class="abs logo-panel"><span class="logo-text">HARBOUR 19 COLLECTIVE</span></div>
<div class="abs topbar">
  <svg width="14" height="10" viewBox="0 0 14 10"><rect x="0.5" y="0.5" width="13" height="9" fill="none" stroke="#555"/><path d="M1 1l6 5 6-5" fill="none" stroke="#555"/></svg>
  <span>hello@harbour19collective.example</span>
  <span class="sep"></span>
  <svg width="12" height="12" viewBox="0 0 24 24"><path d="M6.6 10.8a15 15 0 0 0 6.6 6.6l2.2-2.2a1 1 0 0 1 1-.25 11 11 0 0 0 3.6.6 1 1 0 0 1 1 1V20a1 1 0 0 1-1 1A17 17 0 0 1 3 4a1 1 0 0 1 1-1h3.5a1 1 0 0 1 1 1 11 11 0 0 0 .6 3.6 1 1 0 0 1-.25 1z" fill="#555"/></svg>
  <span>555-01-000000</span>
</div>
<div class="abs search">
  <svg width="38" height="34" viewBox="0 0 38 34"><circle cx="17" cy="15" r="6" fill="none" stroke="#fff" stroke-width="2"/><path d="M21.5 19.5l5 5" stroke="#fff" stroke-width="2.5"/></svg>
</div>
<div class="abs socials-top"><span></span><span></span><span></span><span></span></div>
<nav class="abs nav caps"><span>Home</span><span>Services</span><span>Gallery</span><span>Contact Us</span><span>Blog</span></nav>
<div class="abs hero-title">Do Business</div>
<div class="abs hero-sub">while we care your CHILDREN</div>
<div class="abs hero-btn caps">Book Now</div>
<svg class="abs arrows" width="135" height="40" viewBox="0 0 135 40">
  <path d="M40 20H4M14 10L4 20l10 10" fill="none" stroke="#222" stroke-width="3"/>
  <path d="M96 20h36M122 10l10 10-10 10" fill="none" stroke="#222" stroke-width="3"/>
</svg>

<!-- about -->
<div class="abs frame-title about-title"><span class="box">ABOUT US</span></div>
<div class="abs intro about-intro">Lorem ipsum dolor sit amet, consectetur adipiscing<br>elit, sed do eiusmod tempor incididunt ut labore et</div>
<div class="abs rule about-rule"></div>
<p class="abs about-text">Lorem ipsum dolor sit amet, consectetur adipiscing elit, sed do eiusmod tempor incididunt ut labore et dolore magna aliqua. Ut enim ad minim veniam, quis nostrud exercitation ullamco laboris nisi ut aliquip ex ea commodo consequat. Duis aute irure dolor in reprehenderit in voluptate velit esse cillum dolore eu fugiat nulla pariatur. Excepteur sint occaecat cupidatat non proident, sunt in culpa qui officia deserunt mollit anim id est laborum.</p>
<div class="abs more-btn caps">Click for more</div>

<!-- services -->
<section class="abs services"></section>
<div class="abs frame-title services-title"><span class="box">SERVICES</span></div>
<div class="abs intro services-intro">Lorem ipsum dolor sit amet, consectetur adipiscing<br>elit, sed do eiusmod tempor incididunt ut labore et</div>

<div class="abs card" style="left:173px;top:1356px;height:512px">
  <div class="photo" role="img" aria-label="Warm vintage-toned photograph of two toddlers playing together" style="height:330px;background:linear-gradient(160deg,#e4dcc0,#b9a58c 55%,#8a5b4f)"></div>
  <div class="tab caps" style="top:305px">Childcare</div>
  <p class="body" style="top:355px">Lorem ipsum dolor sit amet, consectetur adipiscing elit, sed do eiusmod tempor incididunt ut labore et dolore magna aliqua.</p>
  <div class="btn caps" style="top:467px">More</div>
</div>

<div class="abs card" style="left:465px;top:1356px;height:903px">
  <div class="photo" role="img" aria-label="Top-down photograph of a laptop, notes and glasses on a grey wooden desk" style="height:710px;background:linear-gradient(170deg,#8d9597,#6f777a 50%,#a4a8a6)"></div>
  <div class="tab caps" style="top:695px">Furnished Office</div>
  <p class="body" style="top:745px">Lorem ipsum dolor sit amet, consectetur adipiscing elit, sed do eiusmod tempor incididunt ut labore et dolore magna aliqua.</p>
  <div class="btn caps" style="top:858px">More</div>
</div>

<div class="abs card" style="left:757px;top:1356px;height:512px">
  <div class="photo" role="img" aria-label="Yellow parking zone illustration with cars" style="height:330px;background:linear-gradient(180deg,#f7b500,#f5c400)"></div>
  <div class="tab caps" style="top:305px">Park &amp; Ride</div>
  <p class="body" style="top:355px">Lorem ipsum dolor sit amet, consectetur adipiscing elit, sed do eiusmod tempor incididunt ut labore et dolore magna aliqua.</p>
  <div class="btn caps" style="top:467px">More</div>
</div>

<div class="abs card" style="left:173px;top:1895px;height:512px">
  <div class="photo" role="img" aria-label="Photograph of a person with a styled copper hair cut on a lime background" style="height:330px;background:linear-gradient(160deg,#d6e08a,#c9b27a 50%,#b9703f)"></div>
  <div class="tab caps" style="top:305px">Hair &amp; Beauty</div>
  <p class="body" style="top:355px">Lorem ipsum dolor sit amet, consectetur adipiscing elit, sed do eiusmod tempor incididunt ut labore et dolore magna aliqua.</p>
  <div class="btn caps" style="top:467px">More</div>
</div>

<div class="abs card" style="left:757px;top:1895px;height:512px">
  <div class="photo" role="img" aria-label="Sepia photograph of a gym with rows of dumbbells" style="height:330px;background:linear-gradient(160deg,#d8d2b6,#8c8772 55%,#4a473b)"></div>
  <div class="tab caps" style="top:305px">Gymnasium</div>
  <p class="body" style="top:355px">Lorem ipsum dolor sit amet, consectetur adipiscing elit, sed do eiusmod tempor incididunt ut labore et dolore magna aliqua.</p>
  <div class="btn caps" style="top:467px">More</div>
</div>

<div class="abs book-btn caps">Book Now</div>

<!-- banner -->
<div class="abs banner" role="img" aria-label="Golden-tinted photograph of a smiling couple outdoors"></div>
<h2 class="abs banner-title caps">Lorem Ipsum Dolor Sit</h2>
<div class="abs banner-rule"></div>
<p class="abs banner-text">At vero eos et accusamus et iusto odio dignissimos ducimus qui blanditiis praesentium voluptatum deleniti atque corrupti quos dolores et quas molestias excepturi sint.</p>

<!-- map -->
<div class="abs map" role="img" aria-label="Street map of South Perth showing the centre location"></div>
<svg class="abs" style="left:574px;top:3165px" width="52" height="120" viewBox="0 0 52 120">
  <circle cx="26" cy="26" r="22" fill="#fff" stroke="#555" stroke-width="2"/>
  <text x="26" y="33" text-anchor="middle" font-family="Montserrat, sans-serif" font-weight="700" font-size="18" fill="#444">19</text>
  <path d="M26 70c-9 0-15 7-15 15 0 11 15 28 15 28s15-17 15-28c0-8-6-15-15-15z" fill="#555"/>
  <circle cx="26" cy="85" r="5" fill="#c9ecfb"/>
</svg>
<div class="abs contact-strip">
  <div class="cell">
    <svg width="22" height="32" viewBox="0 0 22 32"><path d="M11 0C5 0 0 5 0 11c0 8 11 21 11 21s11-13 11-21C22 5 17 0 11 0z" fill="#444"/><circle cx="11" cy="11" r="4" fill="#fff"/></svg>
    <span>48 QUAYLINE RD,<br>SOUTH PERTH, AU 6151</span>
  </div>
  <div class="cell">
    <svg width="28" height="28" viewBox="0 0 24 24"><path d="M6.6 10.8a15 15 0 0 0 6.6 6.6l2.2-2.2a1 1 0 0 1 1-.25 11 11 0 0 0 3.6.6 1 1 0 0 1 1 1V20a1 1 0 0 1-1 1A17 17 0 0 1 3 4a1 1 0 0 1 1-1h3.5a1 1 0 0 1 1 1 11 11 0 0 0 .6 3.6 1 1 0 0 1-.25 1z" fill="#444"/></svg>
    <span>(08) 5550 1919</span>
  </div>
  <div class="cell">
    <svg width="34" height="24" viewBox="0 0 34 24"><rect width="34" height="24" fill="#444"/><path d="M1 1l16 12L33 1" fill="none" stroke="#fff" stroke-width="2"/></svg>
    <span>hello@harbour19.example</span>
  </div>
</div>

<!-- footer -->
<div class="abs foot-logo"><span>HARBOUR 19 COLLECTIVE</span></div>
<div class="abs news-label">Subscribe to our Newsletter</div>
<div class="abs news-input">Your email</div>
<div class="abs news-btn caps">Sign up</div>
<div class="abs socials-foot"><span></span><span></span><span></span><span></span></div>
<footer class="abs bottom-bar">
  <span class="copy">Copyright Information</span>
  <span class="links"><span>Home</span><span>About Us</span><span>Child Care</span><span>Furnished Office</span><span>Park &amp; Ride</span><span>Hair &amp; Beauty</span><span>Gymnasium</span><span>Booking</span><span>Gallery</span><span>Contact Us</span><span>Terms &amp; Conditions</span></span>
</footer>

</body>
</html>
```